Gobal construction supply company needs new business card design

I need a business card design for my global supply company using an existing logo. i will be looking to print these on rounded corner cards with the black background version of my logo on the back. on the front white background, my logo again and my simple details.

```html
<!DOCTYPE html>
<html lang="en">
<head>
<meta charset="utf-8">
<title>Meridian Build Supply – Business Card</title>
<link href="https://fonts.googleapis.com/css2?family=Montserrat:wght@700&family=Roboto:wght@400;500&display=swap" rel="stylesheet">
<style>
  :root {
    --canvas: #2b2b2c;
    --card-white: #ffffff;
    --card-black: #221f20;
    --card-black-light: #353132;
    --brand-red: #e01f26;
    --ink: #231f20;
    --text-grey: #333333;
  }
  * { margin: 0; padding: 0; box-sizing: border-box; }
  html, body { width: 1200px; height: 930px; overflow: hidden; background: var(--canvas); }
  .canvas { position: relative; width: 1200px; height: 930px; }

  .card {
    position: absolute;
    width: 720px;
    height: 412px;
    border-radius: 22px;
    overflow: hidden;
  }

  /* Back side */
  .card--back {
    left: 60px; top: 40px;
    background: radial-gradient(ellipse at 40% 35%, var(--card-black-light), var(--card-black) 70%);
  }
  .card--back .map-area {
    position: absolute; left: 90px; top: 70px; width: 540px; height: 270px;
    border-radius: 40px;
    background: radial-gradient(ellipse at center, rgba(255,255,255,0.07), rgba(255,255,255,0) 70%);
  }
  .card--back .brand {
    position: absolute; left: 0; right: 0; top: 170px;
    display: flex; align-items: center; justify-content: center; gap: 16px;
  }
  .card--back .brand-name { color: #ffffff; font-size: 34px; }

  .brand-dot { width: 22px; height: 22px; border-radius: 50%; background: var(--brand-red); flex: none; }
  .brand-name {
    font-family: "Montserrat", sans-serif; font-weight: 700;
    letter-spacing: 0.5px; text-transform: uppercase; white-space: nowrap;
  }

  /* Front side */
  .card--front { left: 420px; top: 478px; background: var(--card-white); }
  .card--front .brand {
    position: absolute; left: 44px; top: 118px;
    display: flex; align-items: center; gap: 10px;
  }
  .card--front .brand-dot { width: 16px; height: 16px; }
  .card--front .brand-name { color: var(--ink); font-size: 20px; }

  .person { position: absolute; right: 52px; top: 100px; text-align: right; }
  .person-name {
    font-family: "Roboto", sans-serif; font-weight: 500; font-size: 30px;
    color: var(--brand-red); text-transform: uppercase; letter-spacing: -0.5px;
  }
  .person-role { font-family: "Roboto", sans-serif; font-size: 17px; color: var(--text-grey); margin-top: 2px; }

  .divider { position: absolute; left: 44px; right: 44px; top: 196px; height: 2px; background: var(--brand-red); }

  .contacts {
    position: absolute; left: 44px; top: 218px; list-style: none;
    font-family: "Roboto", sans-serif; font-size: 17px; color: var(--text-grey);
  }
  .contacts li { display: flex; align-items: center; gap: 10px; height: 26px; }
  .contacts svg { width: 13px; height: 13px; flex: none; }
  .contacts .accent { color: var(--brand-red); }

  .address {
    position: absolute; right: 52px; top: 218px; text-align: right;
    font-family: "Roboto", sans-serif; font-size: 17px; line-height: 24px; color: var(--text-grey);
  }

  .swoosh { position: absolute; left: 0; bottom: 0; width: 720px; height: 120px; }
</style>
</head>
<body>
<main class="canvas">

  <section class="card card--back" aria-label="Business card back">
    <div class="map-area" role="img" aria-label="Faint dotted world map"></div>
    <div class="brand">
      <span class="brand-dot"></span>
      <span class="brand-name">Meridian Build Supply</span>
    </div>
  </section>

  <section class="card card--front" aria-label="Business card front">
    <div class="brand">
      <span class="brand-dot"></span>
      <span class="brand-name">Meridian Build Supply</span>
    </div>

    <div class="person">
      <p class="person-name">Daniel Archer</p>
      <p class="person-role">Director</p>
    </div>

    <div class="divider"></div>

    <ul class="contacts">
      <li>
        <svg viewBox="0 0 16 16" aria-hidden="true"><path fill="#e01f26" d="M3 1h3l1.5 4-2 1.3a8 8 0 0 0 4.2 4.2L11 8.5l4 1.5v3a2 2 0 0 1-2 2C6.4 15 1 9.6 1 3a2 2 0 0 1 2-2z"/></svg>
        403-555-0142
      </li>
      <li>
        <svg viewBox="0 0 16 16" aria-hidden="true"><rect x="1.5" y="3" width="13" height="10" rx="1" fill="none" stroke="#e01f26" stroke-width="1.6"/><path d="M2 4l6 5 6-5" fill="none" stroke="#e01f26" stroke-width="1.6"/></svg>
        info@meridianbuild.com
      </li>
      <li>
        <svg viewBox="0 0 16 16" aria-hidden="true"><circle cx="8" cy="8" r="6.5" fill="none" stroke="#e01f26" stroke-width="1.4"/><ellipse cx="8" cy="8" rx="3" ry="6.5" fill="none" stroke="#e01f26" stroke-width="1.2"/><path d="M1.5 8h13" stroke="#e01f26" stroke-width="1.2"/></svg>
        <span>www.<span class="accent">meridianbuild</span>.com</span>
      </li>
    </ul>

    <address class="address" style="font-style: normal;">
      48 Quarry Road Box<br>2107, Red Deer, AB
    </address>

    <svg class="swoosh" viewBox="0 0 720 120" preserveAspectRatio="none" aria-hidden="true">
      <path d="M0 96 L440 86 C470 85 470 58 510 56 L720 52 L720 120 L0 120 Z" fill="#e01f26"/>
      <path d="M0 92 L430 80 C455 79 458 68 470 62 L472 66 C462 74 458 86 432 87 L0 100 Z" fill="#231f20"/>
      <path d="M0 101 L432 89 L440 91 L0 104 Z" fill="#ffffff"/>
    </svg>
  </section>

</main>
</body>
</html>
```